KRV Ltd Business Card
Professional Biz Card for Kestrel Ridge Ventures IBC Ltd
KRV Ltd Business Card -
Creative Brief
Professional
Milo Harwick
President & CEO
milo@kestrelridgeventures.biz
www.kestrelridgeventures.biz
Skype ID: mharwick should be added.
www.kestrelridgeventures.biz & perhaps a large version of my logo.

```html
<!DOCTYPE html>
<html lang="en">
<head>
<meta charset="utf-8">
<title>KRV Ltd Stationery Set</title>
<link href="https://fonts.googleapis.com/css2?family=Montserrat:wght@400;600;800&display=swap" rel="stylesheet">
<style>
:root{
  --backdrop:#9c9c9c;
  --frame:#b4b4b4;
  --paper:#ffffff;
  --ink:#111111;
  --band:#161616;
  --silver:#c9c9c9;
  --grey-text:#8a8a8a;
  --light-text:#e6e6e6;
}
*{box-sizing:border-box;margin:0;padding:0}
html,body{width:1200px;height:684px;overflow:hidden;background:var(--backdrop);font-family:"Montserrat",Arial,sans-serif}
.canvas{position:relative;width:1200px;height:684px;background:var(--backdrop);border:6px solid var(--frame)}
.sheet{position:absolute;background:var(--paper);box-shadow:0 1px 3px rgba(0,0,0,.25);overflow:hidden}
.band{position:absolute;left:0;right:0;background:var(--band)}
.brand{position:absolute;font-weight:800;letter-spacing:.08em;white-space:nowrap;line-height:1}
.brand--light{color:var(--light-text)}
.brand--silver{color:var(--silver)}
.contact{position:absolute;color:var(--light-text);font-size:6px;line-height:11px;white-space:nowrap}
.contact--dark{color:var(--ink)}
.contact i{display:inline-block;width:4px;height:4px;background:currentColor;border-radius:50%;margin-right:4px;vertical-align:middle}
.footnote{position:absolute;font-size:6px;color:var(--light-text);white-space:nowrap}

/* letterhead */
.letterhead{left:186px;top:0;width:450px;height:640px}
.letterhead .band--head{top:0;height:120px}
.letterhead .band--foot{bottom:0;height:36px}
.letterhead .brand{left:28px;top:40px;font-size:40px}
.letterhead .contact{right:14px;top:6px}
.letterhead .footnote{right:40px;top:15px}

/* business card */
.card{left:30px;width:153px}
.card--front{top:246px;height:114px}
.card--back{top:362px;height:124px}
.card--front .band--top{top:0;height:17px}
.card .name{position:absolute;left:7px;top:6px;font-size:5px;color:var(--light-text);white-space:nowrap}
.card--front .brand{left:7px;top:26px;font-size:14px}
.card--front .contact{left:7px;top:50px;font-size:4.5px;line-height:8px}
.card--front .contact i{width:3px;height:3px;margin-right:3px}
.card--back .brand{left:7px;top:30px;font-size:18px}
.card--back .band--foot{bottom:0;height:12px}
.card--back .footnote{top:4px;font-size:4.5px}
.card--back .footnote--web{left:7px}
.card--back .footnote--skype{right:7px}

/* envelope back */
.env-back{left:648px;top:172px;width:530px;height:190px;background:var(--band)}
.env-back svg{position:absolute;left:0;top:0}
.env-back .brand{left:50%;top:28px;transform:translateX(-50%);font-size:18px}

/* envelope front */
.env-front{left:648px;top:372px;width:530px;height:214px}
.env-front .band--mid{top:8px;height:66px}
.env-front .brand{left:26px;top:24px;font-size:34px}
.env-front .contact{right:70px;top:14px}
.env-front .footnote{right:40px;bottom:12px;color:var(--grey-text)}
</style>
</head>
<body>
<main class="canvas">

  <section class="sheet letterhead" aria-label="Letterhead">
    <div class="band band--head"></div>
    <div class="brand brand--light">KRV Ltd</div>
    <div class="contact">
      <div><i></i>+44 20 7946 0321</div>
      <div><i></i>www.kestrelridgeventures.biz</div>
      <div><i></i>milo@kestrelridgeventures.biz</div>
    </div>
    <div class="band band--foot"><span class="footnote">Skype ID: mharwick</span></div>
  </section>

  <section class="sheet card card--front" aria-label="Business card front">
    <div class="band band--top"><span class="name">Milo Harwick | President &amp; CEO</span></div>
    <div class="brand brand--silver">KRV Ltd</div>
    <div class="contact contact--dark">
      <div><i></i>+44 20 7946 0321</div>
      <div><i></i>www.kestrelridgeventures.biz</div>
      <div><i></i>milo@kestrelridgeventures.biz</div>
      <div><i></i>Skype ID: mharwick</div>
    </div>
  </section>

  <section class="sheet card card--back" aria-label="Business card back">
    <div class="brand brand--silver">KRV Ltd</div>
    <div class="band band--foot">
      <span class="footnote footnote--web">www.kestrelridgeventures.biz</span>
      <span class="footnote footnote--skype">Skype ID: mharwick</span>
    </div>
  </section>

  <section class="sheet env-back" aria-label="Envelope back">
    <svg width="530" height="190" viewBox="0 0 530 190">
      <path d="M0 0H530V28C455 76 350 110 265 110S75 76 0 28Z" fill="#ffffff"/>
    </svg>
    <div class="brand brand--silver">KRV Ltd</div>
  </section>

  <section class="sheet env-front" aria-label="Envelope front">
    <div class="band band--mid">
      <div class="brand brand--light">KRV Ltd</div>
      <div class="contact">
        <div><i></i>+44 20 7946 0321</div>
        <div><i></i>www.kestrelridgeventures.biz</div>
        <div><i></i>milo@kestrelridgeventures.biz</div>
      </div>
    </div>
    <span class="footnote">Skype ID: mharwick</span>
  </section>

</main>
</body>
</html>
```